DL size Flyer

Design for DL Flyer double sided. One side for blocked drains and pipe relining.
Other side for general plumbing. eg leaking taps, leaking toilets, burst pipes, cctv inspections, gas installations, blocked drains.
Your local plumbing experts.
Relining pictures similar to what we need designed.

Phone number is 0487 312 564 ( on both sides)
Logo for payment methods: cash, quon, cheque. ( on both sides)

Plumbing

```html
<!DOCTYPE html>
<html lang="en">
<head>
<meta charset="utf-8">
<title>Ridgeline Plumbing &amp; Drainage – DL Flyer</title>
<link rel="stylesheet" href="https://fonts.googleapis.com/css2?family=Archivo:wght@700;800;900&family=Open+Sans:ital,wght@0,600;1,600&display=swap">
<style>
  :root {
    --brand-blue: #1a6fba;
    --brand-red: #e31e26;
    --band-light: #1ea6e2;
    --band-dark: #0b5aa0;
    --ink: #333333;
    --ink-soft: #4a4a4a;
    --paper: #ffffff;
    --page: #ececec;
    --ring: #d9d9d9;
    --cash: #5aa532;
    --cheque: #7a7a7a;
    --photo-garden: #8c9677;
    --photo-plumber: #7c9cc6;
    --thumb-before: #b48a78;
    --thumb-after: #7fae6c;
    --thumb-tap: #c4cad0;
    --thumb-toilet: #e3e7eb;
  }
  * { box-sizing: border-box; margin: 0; padding: 0; }
  html, body { width: 1200px; height: 1148px; overflow: hidden; background: var(--page); }
  .spread { position: relative; width: 1200px; height: 1148px; }

  .flyer {
    position: absolute; top: 134px; width: 420px; height: 872px;
    background: var(--paper); overflow: hidden;
    box-shadow: 0 3px 10px rgba(0,0,0,.18);
    font-family: "Open Sans", Arial, sans-serif;
  }
  .flyer--relining { left: 151px; }
  .flyer--general { left: 624px; }

  .photo { position: absolute; left: 0; width: 420px; }
  .photo--garden { top: 90px; height: 470px; background: var(--photo-garden); }
  .photo--plumber { top: 0; height: 310px; background: var(--photo-plumber); }

  .overlay { position: absolute; left: 0; top: 0; width: 420px; height: 872px; }

  .thumb {
    position: absolute; width: 116px; height: 116px; border-radius: 50%;
    border: 6px solid var(--paper); box-shadow: 0 0 0 2px var(--ring), 0 3px 6px rgba(0,0,0,.3);
  }
  .thumb__label {
    position: absolute; top: 20px; width: 100%; text-align: center;
    font: italic 800 12px "Archivo", Arial, sans-serif; color: var(--paper);
  }
  .thumb--before { left: 150px; top: 441px; background: var(--thumb-before); }
  .thumb--after { left: 282px; top: 446px; background: var(--thumb-after); }
  .thumb--tap { left: 147px; top: 200px; background: var(--thumb-tap); }
  .thumb--toilet { left: 274px; top: 200px; background: var(--thumb-toilet); }

  .brand { position: absolute; left: 0; width: 420px; display: flex; justify-content: center; align-items: center; gap: 10px; }
  .brand--top { top: 24px; }
  .brand--mid { top: 352px; }
  .brand__dot { width: 22px; height: 22px; border-radius: 50%; background: var(--brand-blue); flex: none; }
  .brand__name {
    font: 900 30px/1 "Archivo", Arial, sans-serif; color: var(--brand-red);
    text-transform: uppercase; letter-spacing: .5px; text-align: left;
  }
  .brand__name small { display: block; font-size: 15px; letter-spacing: 2.5px; margin-top: 4px; }

  .headline {
    position: absolute; left: 0; width: 420px; text-align: center;
    font: 900 29px/37px "Archivo", Arial, sans-serif; text-transform: uppercase; letter-spacing: .3px;
  }
  .headline--relining { top: 572px; }
  .headline .blue { color: var(--brand-blue); display: block; }
  .headline .red { color: var(--brand-red); display: block; }
  .headline--general { top: 446px; color: var(--brand-blue); }

  .tagline { position: absolute; left: 0; width: 420px; text-align: center;
    font: italic 600 18px/25px "Open Sans", Arial, sans-serif; color: var(--ink-soft); }
  .tagline--relining { top: 657px; }
  .tagline--general { top: 681px; font-size: 15.5px; line-height: 22px; }

  .slogan { position: absolute; top: 718px; left: 0; width: 420px; text-align: center;
    font: 800 20px "Archivo", Arial, sans-serif; color: var(--ink); }

  .services { position: absolute; top: 556px; left: 27px; width: 380px;
    display: grid; grid-template-columns: 183px 197px; row-gap: 13px; list-style: none; }
  .services li { display: flex; align-items: center; gap: 5px;
    font: 600 18.5px/24px "Open Sans", Arial, sans-serif; color: var(--ink); }
  .services svg { width: 17px; height: 17px; flex: none; }

  .payments { position: absolute; top: 754px; left: 0; width: 420px; display: flex; justify-content: center; gap: 4px; z-index: 2; }
  .payment { width: 38px; height: 36px; border-radius: 5px; border: 2px solid var(--paper); box-shadow: 0 1px 3px rgba(0,0,0,.35); }
  .payment--cash { background: var(--cash); }
  .payment--cheque { background: var(--cheque); }
  .payment--quon { background: var(--paper); display: flex; align-items: center; justify-content: center;
    font: italic 800 12px "Archivo", Arial, sans-serif; color: var(--brand-blue); }

  .contact { position: absolute; left: 0; width: 420px; top: 802px; text-align: center; color: var(--paper); z-index: 2; }
  .contact__phone { display: flex; justify-content: center; align-items: center; gap: 8px;
    font: 800 26px "Archivo", Arial, sans-serif; letter-spacing: .5px; }
  .contact__phone svg { width: 22px; height: 22px; }
  .contact__address { margin-top: 6px; font: 600 12.5px "Open Sans", Arial, sans-serif; }
</style>
</head>
<body>
<main class="spread">

  <section class="flyer flyer--relining">
    <div class="photo photo--garden" role="img" aria-label="Photo of a suburban house and lawn with tree roots breaking into an underground drain pipe"></div>
    <svg class="overlay" viewBox="0 0 420 872" aria-hidden="true">
      <defs>
        <linearGradient id="bandA" x1="0" x2="1"><stop offset="0" stop-color="var(--band-light)"/><stop offset="1" stop-color="var(--band-dark)"/></linearGradient>
      </defs>
      <path d="M0,0 H420 V92 Q250,150 0,98 Z" fill="var(--paper)"/>
      <path d="M0,98 Q250,150 420,92" fill="none" stroke="var(--brand-red)" stroke-width="7"/>
      <path d="M0,548 Q200,490 420,505 V872 H0 Z" fill="var(--paper)"/>
      <path d="M0,548 Q200,490 420,505" fill="none" stroke="var(--brand-red)" stroke-width="8"/>
      <path d="M0,793 Q210,735 420,793" fill="none" stroke="#cfcfcf" stroke-width="3"/>
      <path d="M0,800 Q210,745 420,800 V872 H0 Z" fill="url(#bandA)"/>
    </svg>
    <div class="brand brand--top">
      <span class="brand__dot"></span>
      <span class="brand__name">Ridgeline<small>Plumbing &amp; Drainage</small></span>
    </div>
    <div class="thumb thumb--before" role="img" aria-label="Photo inside a root-blocked pipe before relining"><span class="thumb__label">BEFORE</span></div>
    <div class="thumb thumb--after" role="img" aria-label="Photo inside a relined pipe after repair"><span class="thumb__label">AFTER</span></div>
    <h1 class="headline headline--relining"><span class="blue">Blocked drains &amp;</span><span class="red">Pipe relining</span></h1>
    <p class="tagline tagline--relining">A fast, clean, permanent solution<br>for fixing blocked drains.</p>
    <p class="slogan">Your local plumbing experts.</p>
    <div class="payments"><span class="payment payment--cash"></span><span class="payment payment--cheque"></span><span class="payment payment--quon">quon</span></div>
    <div class="contact">
      <div class="contact__phone"><svg viewBox="0 0 24 24"><path fill="currentColor" d="M6.6 10.8a15 15 0 0 0 6.6 6.6l2.2-2.2c.3-.3.7-.4 1-.2 1.1.4 2.3.6 3.6.6.6 0 1 .4 1 1V20c0 .6-.4 1-1 1A17 17 0 0 1 3 4c0-.6.4-1 1-1h3.5c.6 0 1 .4 1 1 0 1.3.2 2.5.6 3.6.1.3 0 .7-.2 1z"/></svg>0487 312 564</div>
      <p class="contact__address">27 Wattle Lane, 2999 Sydney - Greenvale New South Wales</p>
    </div>
  </section>

  <section class="flyer flyer--general">
    <div class="photo photo--plumber" role="img" aria-label="Photo of a plumber in blue overalls fixing pipework under a sink"></div>
    <svg class="overlay" viewBox="0 0 420 872" aria-hidden="true">
      <defs>
        <linearGradient id="bandB" x1="0" x2="1"><stop offset="0" stop-color="var(--band-light)"/><stop offset="1" stop-color="var(--band-dark)"/></linearGradient>
      </defs>
      <path d="M0,330 Q200,270 420,262 V872 H0 Z" fill="var(--paper)"/>
      <path d="M0,320 Q200,262 420,255" fill="none" stroke="var(--brand-red)" stroke-width="16"/>
      <path d="M0,793 Q210,735 420,793" fill="none" stroke="#cfcfcf" stroke-width="3"/>
      <path d="M0,800 Q210,745 420,800 V872 H0 Z" fill="url(#bandB)"/>
    </svg>
    <div class="thumb thumb--tap" role="img" aria-label="Photo of a wrench on a chrome tap"></div>
    <div class="thumb thumb--toilet" role="img" aria-label="Photo of a toilet being repaired"></div>
    <div class="brand brand--mid">
      <span class="brand__dot"></span>
      <span class="brand__name">Ridgeline<small>Plumbing &amp; Drainage</small></span>
    </div>
    <h1 class="headline headline--general">Your local<br>plumbing experts</h1>
    <ul class="services">
      <li><svg viewBox="0 0 18 18"><circle cx="9" cy="9" r="7.5" fill="none" stroke="var(--brand-blue)" stroke-width="1.6"/><path d="M5.5 9.2l2.4 2.3 4.6-4.8" fill="none" stroke="var(--brand-blue)" stroke-width="1.8"/></svg>Leaking taps</li>
      <li><svg viewBox="0 0 18 18"><circle cx="9" cy="9" r="7.5" fill="none" stroke="var(--brand-blue)" stroke-width="1.6"/><path d="M5.5 9.2l2.4 2.3 4.6-4.8" fill="none" stroke="var(--brand-blue)" stroke-width="1.8"/></svg>CCTV inspections</li>
      <li><svg viewBox="0 0 18 18"><circle cx="9" cy="9" r="7.5" fill="none" stroke="var(--brand-blue)" stroke-width="1.6"/><path d="M5.5 9.2l2.4 2.3 4.6-4.8" fill="none" stroke="var(--brand-blue)" stroke-width="1.8"/></svg>Leaking toilets</li>
      <li><svg viewBox="0 0 18 18"><circle cx="9" cy="9" r="7.5" fill="none" stroke="var(--brand-blue)" stroke-width="1.6"/><path d="M5.5 9.2l2.4 2.3 4.6-4.8" fill="none" stroke="var(--brand-blue)" stroke-width="1.8"/></svg>Gas installations</li>
      <li><svg viewBox="0 0 18 18"><circle cx="9" cy="9" r="7.5" fill="none" stroke="var(--brand-blue)" stroke-width="1.6"/><path d="M5.5 9.2l2.4 2.3 4.6-4.8" fill="none" stroke="var(--brand-blue)" stroke-width="1.8"/></svg>Burst pipes</li>
      <li><svg viewBox="0 0 18 18"><circle cx="9" cy="9" r="7.5" fill="none" stroke="var(--brand-blue)" stroke-width="1.6"/><path d="M5.5 9.2l2.4 2.3 4.6-4.8" fill="none" stroke="var(--brand-blue)" stroke-width="1.8"/></svg>Blocked drains</li>
    </ul>
    <p class="tagline tagline--general">Provides a solution to the whole problem,<br>not just temporary relief from the symptoms.</p>
    <div class="payments"><span class="payment payment--cash"></span><span class="payment payment--cheque"></span><span class="payment payment--quon">quon</span></div>
    <div class="contact">
      <div class="contact__phone"><svg viewBox="0 0 24 24"><path fill="currentColor" d="M6.6 10.8a15 15 0 0 0 6.6 6.6l2.2-2.2c.3-.3.7-.4 1-.2 1.1.4 2.3.6 3.6.6.6 0 1 .4 1 1V20c0 .6-.4 1-1 1A17 17 0 0 1 3 4c0-.6.4-1 1-1h3.5c.6 0 1 .4 1 1 0 1.3.2 2.5.6 3.6.1.3 0 .7-.2 1z"/></svg>0487 312 564</div>
      <p class="contact__address">27 Wattle Lane, 2999 Sydney - Greenvale New South Wales</p>
    </div>
  </section>

</main>
</body>
</html>
```